Social Movement/Church Plant Website - KindHearth.com

We need a website for our church plant startup, however we want the focus of the landing page to be around #kindhearth - that we are an organization that is FOR our town (Cedarvale). The site will include serving project events, social events, a place to sign up for emails, a blog, a place to give, etc. All the elements we know we want are currently at kindhearth.com . Please check this for copy.

We want this to be easy to edit as a non-developer.

I have included several logos with our colors, as well as an ai file to give you an idea of how we want the design to look and feel - also includes our branded fonts

Target Market(s)

People who live in the Northern CO area

Font styles to use
Serif
Sans Serif

Requirements
Must have
• Events (serve and social), Blog section, A place to get involved - where to give and to sign up for emails. Must match our branding colors and style hex 4c7991.
Should not have
• Should not be focused on the actual church plant on the home page. There can be some back end stuff about it, but the focus should be #kindhearth.

```html
<!DOCTYPE html>
<html lang="en">
<head>
<meta charset="utf-8">
<title>KindHearth — For Our Town</title>
<link rel="stylesheet" href="https://fonts.googleapis.com/css2?family=Montserrat:wght@400;600;700;800&family=Open+Sans:wght@400;600;700&display=swap">
<style>
:root{
  --brand:#4c7991;
  --brand-deep:#3d6a82;
  --brand-dark:#33596e;
  --red:#ef4651;
  --sky:#2ba3e6;
  --sun:#f5b800;
  --ink:#2b2b2b;
  --ink-soft:#555;
  --bar:#3a3a3a;
  --line:#e4e4e4;
  --white:#fff;
}
*{box-sizing:border-box;margin:0;padding:0}
html,body{width:1200px;height:3317px;overflow:hidden}
body{font-family:"Open Sans",Arial,sans-serif;color:var(--ink);background:var(--white);position:relative}
.abs{position:absolute}
h1,h2,h3,h4,.btn,.nav a{font-family:"Montserrat",Arial,sans-serif}
.btn{display:inline-flex;align-items:center;justify-content:center;border-radius:30px;font-weight:700;color:var(--white);text-decoration:none}

/* top bar */
.topbar{left:0;top:0;width:1200px;height:36px;background:var(--bar)}
.topbar .donate{position:absolute;left:751px;top:0;width:121px;height:36px;background:var(--red);color:#fff;font:700 10px "Montserrat",sans-serif;display:flex;align-items:center;justify-content:center;letter-spacing:.5px}
.topbar .social{position:absolute;left:890px;top:13px;display:flex;gap:13px}
.topbar .social span{width:10px;height:10px;border-radius:50%;background:#ddd}

/* nav */
.header{left:0;top:36px;width:1200px;height:75px;background:#fff}
.brand{position:absolute;left:166px;top:9px;display:flex;align-items:center;gap:10px}
.brand .mark{width:55px;height:55px;background:var(--brand);border-radius:6px}
.brand .name{font:700 20px "Montserrat",sans-serif;color:var(--brand)}
.nav{position:absolute;right:155px;top:34px;display:flex;gap:32px}
.nav a{font-size:11px;font-weight:600;color:var(--ink);text-decoration:none;letter-spacing:.3px}

/* hero */
.hero{left:0;top:111px;width:1200px;height:469px;background:linear-gradient(90deg,#3b3330 0%,#6d5a4e 45%,#8a7a70 70%,#4d4540 100%)}
.hero h1{position:absolute;left:160px;top:96px;width:560px;color:#fff;font-size:27px;line-height:33px;font-weight:800;text-transform:uppercase}
.hero p{position:absolute;left:160px;top:210px;width:330px;color:#fff;font-size:11px;line-height:14px}
.hero .btn{position:absolute;left:166px;top:299px;width:151px;height:40px;background:var(--brand);font-size:14px}

/* story */
.story-photo{left:0;top:580px;width:620px;height:465px;background:linear-gradient(135deg,#cfd9c2 0%,#8aa06a 40%,#5b7340 70%,#3e4f2c 100%)}
.story{left:620px;top:580px;width:580px;height:465px;background:var(--brand-deep);color:#fff}
.story h2{position:absolute;left:53px;top:64px;font-size:21px;font-weight:800;letter-spacing:.5px}
.story h3{position:absolute;left:53px;top:98px;font-size:17px;font-weight:700}
.story .copy{position:absolute;left:53px;top:137px;width:378px;font-size:10.5px;line-height:16px}
.story .copy p+p{margin-top:16px}
.story .btn{position:absolute;left:53px;top:356px;width:133px;height:34px;background:var(--red);font-size:12px}

/* section headings */
.sec-title{left:0;width:1200px;text-align:center;font:800 21px "Montserrat",sans-serif;color:var(--ink)}
.sec-title em{font-style:normal;color:var(--brand)}

/* events */
.event{top:1158px;width:275px;height:370px;color:#fff}
.event .photo{height:170px}
.event .body{height:200px;padding:20px 22px;position:relative}
.event .date{font-size:10px;margin-bottom:14px}
.event h4{font-size:10.5px;font-weight:700;margin-bottom:10px}
.event p{font-size:10px;line-height:19px}
.event .btn{position:absolute;left:50%;transform:translateX(-50%);bottom:22px;width:118px;height:30px;background:var(--ink);font-size:11px}
.event.red .body{background:var(--red)}
.event.blue .body{background:var(--brand-deep)}

/* testimonials */
.voices{left:0;top:1625px;width:1200px;height:407px;background:var(--brand-deep)}
.voices h2{position:absolute;left:0;top:50px;width:1200px;text-align:center;color:#fff;font-size:21px;font-weight:800}
.quote{position:absolute;left:186px;top:120px;width:828px;height:168px;background:#fff;border-radius:12px;padding:26px 40px 0 75px}
.quote .mark{position:absolute;left:26px;top:8px;font:700 78px Georgia,serif;color:var(--red);line-height:1}
.quote p{font-size:12px;line-height:15px;color:#777}
.quote .who{margin-top:24px;text-align:center;font:700 18px "Montserrat",sans-serif;color:var(--ink)}
.quote .who span{color:var(--red)}
.quote::after{content:"";position:absolute;left:262px;bottom:-14px;border:14px solid transparent;border-bottom:0;border-top-color:#fff}
.avatars{position:absolute;left:456px;top:323px;display:flex;gap:12px}
.avatars span{width:48px;height:48px;border-radius:50%;border:3px solid #fff;background:#d9b39a}

/* blog */
.post{left:255px;width:700px;height:150px}
.post .photo{position:absolute;left:0;top:0;width:276px;height:150px}
.post .text{position:absolute;left:298px;top:0;width:400px}
.post h4{font-size:13px;font-weight:600;font-family:"Open Sans",sans-serif;margin-top:2px}
.post .meta{display:flex;gap:16px;font-size:9px;color:#999;margin:12px 0 12px}
.post .meta i{display:inline-block;width:8px;height:8px;border-radius:50%;background:#bbb;margin-right:4px;vertical-align:-1px}
.post p{font-size:10.5px;line-height:15px;color:var(--ink-soft);text-align:justify}
.post .view{position:absolute;left:298px;top:119px;width:90px;height:31px;background:var(--ink);color:#fff;font:600 10px "Montserrat",sans-serif;display:flex;align-items:center;justify-content:center}

/* partner */
.partner{left:0;top:2568px;width:1200px;height:315px;background:linear-gradient(90deg,#2f2b27 0%,#4a4038 40%,#3a352f 70%,#26231f 100%)}
.partner h3{position:absolute;left:0;top:52px;width:1200px;text-align:center;color:#fff;font-size:15px;font-weight:700}
.partner .sub{position:absolute;left:0;top:94px;width:1200px;text-align:center;color:#fff;font-size:17px}
.ways{position:absolute;left:208px;top:151px;display:flex}
.ways a{width:257px;height:53px;display:flex;align-items:center;justify-content:center;gap:12px;color:#fff;font:600 12px "Montserrat",sans-serif;text-decoration:none;text-transform:uppercase}
.ways .involve{background:var(--sky)}
.ways .partnership{background:var(--red)}
.ways .give{background:var(--sun)}
.ways svg{width:22px;height:22px}
.ways .joint{position:absolute;top:19px;width:15px;height:15px;background:#fff;opacity:.85}

/* question bar */
.ask{left:162px;top:2838px;width:874px;height:87px;background:var(--red);color:#fff;z-index:3}
.ask svg{position:absolute;left:22px;top:28px}
.ask .label{position:absolute;left:72px;top:30px;font:700 11px/13px "Montserrat",sans-serif}
.ask .num{position:absolute;left:187px;top:24px;font:700 32px "Montserrat",sans-serif}
.ask .email{position:absolute;left:482px;top:30px;width:237px;height:30px;border-radius:20px;background:#fff}
.ask .email svg{left:10px;top:9px}
.ask .sub{position:absolute;left:734px;top:30px;width:118px;height:30px;background:var(--ink);font-size:12px}

/* footer */
.footer{left:0;top:2883px;width:1200px;height:434px;background:var(--brand-deep);color:#fff}
.footer h4{position:absolute;top:113px;font-size:11px;font-weight:600;letter-spacing:.5px}
.form{position:absolute;left:162px;top:145px;width:248px}
.form .field{border-bottom:1px solid rgba(255,255,255,.6);font-size:9px;padding:4px 0 6px;height:27px}
.form .msg{height:60px}
.form .send{margin-top:20px;width:118px;height:35px;background:var(--red);font:600 10px "Montserrat",sans-serif;display:flex;align-items:center;justify-content:center;text-transform:uppercase}
.links{position:absolute;left:484px;top:150px;list-style:none}
.links li{font-size:11px;margin-bottom:13px;display:flex;align-items:center;gap:12px}
.links li::before{content:"›";display:inline-flex;align-items:center;justify-content:center;width:13px;height:13px;border-radius:50%;background:#fff;color:var(--brand-deep);font-weight:700;font-size:11px;line-height:1}
.insta{position:absolute;left:649px;top:152px;display:grid;grid-template-columns:52px 52px;gap:6px}
.insta span{height:51px;background:linear-gradient(135deg,#c99a7d,#7f6654)}
.contact{position:absolute;left:837px;top:140px;width:230px}
.contact .item{position:relative;padding-left:30px;margin-bottom:22px;font-size:11px;line-height:14px}
.contact .item b{font-weight:600;display:block}
.contact .item .ic{position:absolute;left:0;top:0;width:20px;height:20px;border-radius:50%;background:var(--red);display:flex;align-items:center;justify-content:center}
.copyright{position:absolute;left:0;top:396px;width:1200px;text-align:center;font-size:9px}
</style>
</head>
<body>

<div class="abs topbar">
  <div class="donate">DONATE NOW</div>
  <div class="social"><span></span><span></span><span></span><span></span><span></span><span></span></div>
</div>

<header class="abs header">
  <div class="brand"><span class="mark"></span><span class="name">KindHearth</span></div>
  <nav class="nav">
    <a>HOME</a><a>ABOUT US</a><a>CAUSES</a><a>EVENTS</a><a>BLOG</a><a>GIVE</a><a>CONTACT US</a>
  </nav>
</header>

<section class="abs hero" role="img" aria-label="Neighbours sharing a meal at a long table, a plate of food passed across">
  <h1>A movement to restore hope, strength, and purpose through the Gospel of Jesus.</h1>
  <p>Lorem Ipsum is simply dummy text of the printing and typesetting industry. Lorem Ipsum has been Lorem Ipsum is simply dummy text of the printing and type-setting industry. Lorem Ipsum has been</p>
  <a class="btn">Donate Now</a>
</section>

<div class="abs story-photo" role="img" aria-label="Volunteers smiling while harvesting in a community garden"></div>
<section class="abs story">
  <h2>OUR STORY</h2>
  <h3>Working Toward a Better Tomorrow</h3>
  <div class="copy">
    <p>What if we were known not by what we're against, but by what we're for? If our collective energy was invested in things that unite rather than divide, wouldn't we see stronger neighborhoods, healthier communities, and more resilient relationships? We believe so.</p>
    <p>We are for the broken and the brand new, the beautifully painted and the terribly stained. We are for the addict and the aristocrat, the put together and the never been messier. We are for families and individuals, for the unloved and the unwanted. We are for the workaholic and the in-between-jober, the ones who grew up here and those who just got here. We are for a better tomorrow. We are for our city. We are For Cedarvale.</p>
  </div>
  <a class="btn">Learn More</a>
</section>

<h2 class="abs sec-title" style="top:1080px">UPCOMING <em>EVENTS</em></h2>

<article class="abs event red" style="left:162px">
  <div class="photo" role="img" aria-label="Child swimming at the edge of an outdoor pool" style="background:linear-gradient(180deg,#7cc4e0,#2f8fb8)"></div>
  <div class="body">
    <div class="date">July 26 | 5:30pm - 7:30pm</div>
    <h4>Maple Outdoor Pool</h4>
    <p>Jul 26, 5:30 PM – 7:30 PM, Maple Outdoor Pool, 220 Elm St, Cedarvale, CV 10101, USA. Bring the whole fam for an evening at</p>
    <a class="btn">Register now</a>
  </div>
</article>
<article class="abs event blue" style="left:463px">
  <div class="photo" role="img" aria-label="Volunteers in green shirts cleaning up a school yard" style="background:linear-gradient(180deg,#e6ebe3,#7ea36a)"></div>
  <div class="body">
    <div class="date">July 26 | 5:30pm - 7:30pm</div>
    <h4>School Clean Up</h4>
    <p>Join us to help clean up a local school!</p>
    <a class="btn">Register Now</a>
  </div>
</article>
<article class="abs event blue" style="left:764px">
  <div class="photo" role="img" aria-label="Group building a wooden gaga pit on a school field" style="background:linear-gradient(180deg,#b9a88e,#7d6b52)"></div>
  <div class="body">
    <div class="date">July 26 | 5:30pm - 7:30pm</div>
    <h4>Building Gaga Pit for Local School</h4>
    <p>Jul 14 Ridgeview Classical School Jul 14, 9:00 AM – 12:00 PM Ridgeview Classical School, 415 Birch Ave, Cedarvale, CV 10102, USA</p>
    <a class="btn">Register Now</a>
  </div>
</article>

<section class="abs voices">
  <h2>WHAT PEOPLE SAY</h2>
  <div class="quote">
    <span class="mark">“</span>
    <p>Lorem ipsum dolor sit amet, consectetur adipisicing elit, sed do eiusmod tempor incididunt ut labore et dolore magna aliqua. Ut enim ad minim veniam. Quis nostrud exercitation ullamco laboris nisi ut aliquip ex ea commodo consequat. Duis aute irure dolor Lorem ipsum dolor sit amet, consectetur adipisicing elit, sed do eiusmod tempor incididunt ut labore et dolore magna aliqua. Ut enim ad minim veniam.</p>
    <div class="who"><span>John Doe</span> | NGO</div>
  </div>
  <div class="avatars">
    <span role="img" aria-label="Portrait of a community member"></span>
    <span role="img" aria-label="Portrait of a community member"></span>
    <span role="img" aria-label="Portrait of a community member"></span>
    <span role="img" aria-label="Portrait of a community member"></span>
    <span role="img" aria-label="Portrait of a community member" style="background:#c7b8a8"></span>
  </div>
</section>

<h2 class="abs sec-title" style="top:2098px">OUR <em>BLOG</em></h2>

<article class="abs post" style="top:2179px">
  <div class="photo" role="img" aria-label="Volunteers visiting with an older neighbour outdoors" style="background:linear-gradient(135deg,#9aa889,#5d6b4c)"></div>
  <div class="text">
    <h4>Lorem ipsum dolor sit amet, consectetur</h4>
    <div class="meta"><span><i></i>admin</span><span><i></i>1050</span><span><i></i>1280</span></div>
    <p>Integer ornare libero nisi. Duis ac magna urna. Nulla facilisi. Phasellus at ante magna aliquam. Suspendisse nec porta nulla. Suspendisse nec orci vel elit aliquet blandit in non orci. Vivamus posuere dui eget lacinia rutrum. Cum sociis natoque penatibus ...</p>
  </div>
  <a class="view">VIEW MORE</a>
</article>
<article class="abs post" style="top:2365px">
  <div class="photo" role="img" aria-label="Volunteers laying a gravel path in a yard" style="background:linear-gradient(135deg,#a79a88,#6b5f50)"></div>
  <div class="text">
    <h4>Lorem ipsum dolor sit amet, consectetur</h4>
    <div class="meta"><span><i></i>admin</span><span><i></i>1050</span><span><i></i>1280</span></div>
    <p>Integer ornare libero nisi. Duis ac magna urna. Nulla facilisi. Phasellus at ante magna aliquam. Suspendisse nec porta nulla. Suspendisse nec orci vel elit aliquet blandit in non orci. Vivamus posuere dui eget lacinia rutrum. Cum sociis natoque penatibus ...</p>
  </div>
  <a class="view">VIEW MORE</a>
</article>

<section class="abs partner" role="img" aria-label="Dimmed photo of a smiling volunteer outdoors">
  <h3>INTERESTED IN PARTNERING WITH US?</h3>
  <div class="sub">We would love to partner with you to help in our community!</div>
  <div class="ways">
    <a class="involve"><svg viewBox="0 0 22 22"><circle cx="11" cy="11" r="9" fill="none" stroke="#fff" stroke-width="2"/></svg>Get Involved</a>
    <a class="partnership"><svg viewBox="0 0 22 22"><circle cx="11" cy="11" r="9" fill="none" stroke="#fff" stroke-width="2"/></svg>Partnership</a>
    <a class="give"><svg viewBox="0 0 22 22"><circle cx="11" cy="11" r="9" fill="none" stroke="#fff" stroke-width="2"/></svg>Donate Now</a>
    <span class="joint" style="left:250px"></span>
    <span class="joint" style="left:507px"></span>
  </div>
</section>

<div class="abs ask">
  <svg width="34" height="34" viewBox="0 0 24 24"><path fill="#fff" d="M6.6 10.8a15.1 15.1 0 0 0 6.6 6.6l2.2-2.2c.3-.3.7-.4 1-.2 1.1.4 2.3.6 3.6.6.6 0 1 .4 1 1V20c0 .6-.4 1-1 1A17 17 0 0 1 3 4c0-.6.4-1 1-1h3.5c.6 0 1 .4 1 1 0 1.3.2 2.5.6 3.6.1.3 0 .7-.2 1z"/></svg>
  <div class="label">DO YOU HAVE<br>A QUESTION?</div>
  <div class="num">+0123 456 789</div>
  <div class="email"><svg class="abs" width="14" height="12" viewBox="0 0 14 12"><rect x="0.5" y="0.5" width="13" height="11" rx="1" fill="var(--red)"/><path d="M1 1l6 5 6-5" stroke="#fff" fill="none"/></svg></div>
  <a class="btn sub">Subscribe</a>
</div>

<footer class="abs footer">
  <h4 style="left:162px">CONTACT FORM</h4>
  <div class="form">
    <div class="field">Name</div>
    <div class="field">Email</div>
    <div class="field">Phone</div>
    <div class="field msg">Message</div>
    <div class="send">Send Message</div>
  </div>

  <h4 style="left:480px">QUICK LINKS</h4>
  <ul class="links">
    <li>Home</li><li>About</li><li>Causes</li><li>Event</li><li>News</li><li>Contact</li>
  </ul>

  <h4 style="left:646px">INSTAGRAM</h4>
  <div class="insta">
    <span role="img" aria-label="Community photo"></span>
    <span role="img" aria-label="Community photo"></span>
    <span role="img" aria-label="Community photo"></span>
    <span role="img" aria-label="Community photo"></span>
    <span role="img" aria-label="Community photo"></span>
    <span role="img" aria-label="Community photo"></span>
  </div>

  <h4 style="left:837px">CONTACT US</h4>
  <div class="contact">
    <div class="item"><span class="ic"><svg width="10" height="12" viewBox="0 0 10 12"><path d="M5 0a4 4 0 0 0-4 4c0 3 4 8 4 8s4-5 4-8a4 4 0 0 0-4-4z" fill="#fff"/><circle cx="5" cy="4" r="1.5" fill="var(--red)"/></svg></span><b>Head Office</b>123, Main Street, Your City<br>USA 789456</div>
    <div class="item" style="margin-top:30px"><span class="ic"><svg width="10" height="10" viewBox="0 0 24 24"><path fill="#fff" d="M6.6 10.8a15.1 15.1 0 0 0 6.6 6.6l2.2-2.2c.3-.3.7-.4 1-.2 1.1.4 2.3.6 3.6.6.6 0 1 .4 1 1V20c0 .6-.4 1-1 1A17 17 0 0 1 3 4c0-.6.4-1 1-1h3.5c.6 0 1 .4 1 1 0 1.3.2 2.5.6 3.6.1.3 0 .7-.2 1z"/></svg></span><b>Phone Number</b>+123 456 7890<br>+123 456 7890</div>
    <div class="item" style="margin-top:30px"><span class="ic"><svg width="10" height="8" viewBox="0 0 14 12"><rect width="14" height="12" rx="1" fill="#fff"/><path d="M1 1l6 5 6-5" stroke="var(--red)" fill="none"/></svg></span><b>Email</b>info@kindhearth.com<br>contact@kindhearth.com</div>
  </div>

  <div class="copyright">Copyright © 2018 KindHearth.com . All Rights Reserved.</div>
</footer>

</body>
</html>
```